I am looking for business cards and letterhead

I want a high-level look for CEO's who want a concierge level leadership consultant and organization development strategist

This needs to go with my brand: simple, elegant, clean. Please improve on this design while using these fonts and colors

Here is my website: CorinneHalvers.com

```html
<!DOCTYPE html>
<html lang="en">
<head>
<meta charset="utf-8">
<title>Summit Path Advisory – Stationery</title>
<link href="https://fonts.googleapis.com/css2?family=Montserrat:wght@400;500;600;700&family=Lato:wght@400;700&display=swap" rel="stylesheet">
<style>
:root{
  --navy:#111836;
  --navy-text:#16204a;
  --blue:#1b5fb8;
  --gold:#c9a765;
  --paper:#fbfbfc;
  --grey:#5b5f6b;
  --body:#6c707a;
  --bg:#ebe5dc;
}
*{margin:0;padding:0;box-sizing:border-box}
html,body{width:1200px;height:1067px;overflow:hidden;background:var(--bg)}
.canvas{position:relative;width:1200px;height:1067px}
.card{position:absolute;width:464px;height:265px;border-radius:22px;overflow:hidden;box-shadow:0 6px 14px rgba(0,0,0,.25)}
.card-front{left:75px;top:256px;background:var(--navy)}
.card-back{left:77px;top:546px;background:var(--paper)}
.mark-ring{position:absolute;border-radius:50%;border:3px solid var(--gold)}
.card-front .mark-ring{left:164px;top:37px;width:136px;height:136px}
.brand-name{position:absolute;font-family:"Montserrat",sans-serif;font-weight:600;letter-spacing:.06em;text-transform:uppercase;text-align:center;white-space:nowrap}
.card-front .brand-name{left:0;width:464px;top:190px;font-size:22px;color:#fff}
.card-back .mark-ring{left:72px;top:62px;width:88px;height:88px;border-width:2.5px}
.card-back .brand-name{left:0;width:232px;top:163px;font-size:14px;color:var(--navy-text)}
.divider{position:absolute;left:227px;top:51px;width:2px;height:146px;background:var(--navy)}
.contact{position:absolute;left:250px;top:50px;font-family:"Montserrat",sans-serif;color:var(--navy-text)}
.contact .person{font-size:17px;font-weight:700;letter-spacing:.02em;text-transform:uppercase}
.contact .role{font-size:12.5px;color:var(--grey);margin-top:3px}
.contact .address{font-size:12.5px;color:var(--grey);margin-top:13px;line-height:18px}
.contact ul{list-style:none;margin-top:9px;font-size:12.5px;color:var(--grey)}
.contact li{display:flex;align-items:center;gap:6px;height:19px}
.icon{width:11px;height:11px;flex:none}
.footer-band{position:absolute;left:0;bottom:0;width:100%;background:linear-gradient(180deg,#2a4a8a 0%,var(--navy) 45%,var(--navy) 100%)}
.card-back .footer-band{height:48px}
.letterhead .footer-band{height:70px}
.letterhead{position:absolute;left:573px;top:143px;width:552px;height:782px;background:var(--paper);box-shadow:0 6px 16px rgba(0,0,0,.25);overflow:hidden;font-family:"Lato",sans-serif}
.letterhead .mark-ring{left:72px;top:36px;width:60px;height:60px;border-width:2px}
.letterhead .brand-name{left:30px;width:144px;top:104px;font-size:10.5px;color:var(--navy-text)}
.letter-contact{position:absolute;left:366px;top:44px;padding-left:7px;border-left:1px solid var(--blue);font-family:"Montserrat",sans-serif;font-size:9.5px;color:#222;line-height:13.5px}
.letter-contact ul{list-style:none;margin-top:5px}
.letter-contact li{display:flex;align-items:center;gap:4px}
.letter-contact .icon{width:8px;height:8px}
.watermark{position:absolute;left:102px;top:216px;width:350px;height:350px;border-radius:50%;border:10px solid rgba(17,24,54,.035)}
.recipient{position:absolute;left:45px;top:198px}
.recipient h2{font-size:11.5px;font-weight:700;color:#111}
.recipient p{font-size:8.5px;font-weight:700;color:#222;margin-top:3px}
.date{position:absolute;right:45px;top:212px;font-size:8.5px;color:var(--body)}
.letter-body{position:absolute;left:45px;top:252px;width:462px;font-size:8.4px;line-height:13.5px;color:var(--body);text-align:justify}
.letter-body p+p{margin-top:13px}
.signature{position:absolute;left:45px;top:560px;width:118px;height:36px;background:linear-gradient(90deg,rgba(34,34,34,.15),rgba(34,34,34,.05))}
.sign-off{position:absolute;left:45px;top:608px}
.sign-off h3{font-size:11px;font-weight:700;color:#111}
.sign-off p{font-size:8.5px;font-weight:700;color:var(--body);margin-top:3px}
</style>
</head>
<body>
<main class="canvas">

  <section class="card card-front">
    <div class="mark-ring"></div>
    <div class="brand-name">Summit Path Advisory</div>
  </section>

  <section class="card card-back">
    <div class="mark-ring"></div>
    <div class="brand-name">Summit Path Advisory</div>
    <div class="divider"></div>
    <div class="contact">
      <div class="person">Corinne Halvers</div>
      <div class="role">CEO &amp; Owner</div>
      <div class="address">14/22 Harbour View Rd<br>Kelvin Bay, QLD 4610</div>
      <ul>
        <li><svg class="icon" viewBox="0 0 12 12"><path fill="#1b5fb8" d="M1 4c0-2 2-3 5-3s5 1 5 3v1H8V4H4v1H1zM2 6h8l1 5H1z"/></svg>0412555870</li>
        <li><svg class="icon" viewBox="0 0 12 12"><rect x="1" y="2.5" width="10" height="7" fill="#1b5fb8"/><path d="M1 2.5l5 4 5-4" stroke="#fff" fill="none"/></svg>info@corinnehalvers.com</li>
        <li><svg class="icon" viewBox="0 0 12 12"><circle cx="6" cy="6" r="5" fill="#1b5fb8"/><path d="M1 6h10M6 1c-2 2.5-2 7.5 0 10M6 1c2 2.5 2 7.5 0 10" stroke="#fff" stroke-width=".8" fill="none"/></svg>www.corinnehalvers.com</li>
      </ul>
    </div>
    <div class="footer-band" role="img" aria-label="Decorative footer band in navy, blue and gold"></div>
  </section>

  <section class="letterhead">
    <div class="watermark"></div>
    <div class="mark-ring"></div>
    <div class="brand-name">Summit Path Advisory</div>
    <div class="letter-contact">
      14/22 Harbour View Rd<br>Kelvin Bay, QLD 4610
      <ul>
        <li><svg class="icon" viewBox="0 0 12 12"><path fill="#1b5fb8" d="M1 4c0-2 2-3 5-3s5 1 5 3v1H8V4H4v1H1zM2 6h8l1 5H1z"/></svg>0412555870</li>
        <li><svg class="icon" viewBox="0 0 12 12"><rect x="1" y="2.5" width="10" height="7" fill="#1b5fb8"/><path d="M1 2.5l5 4 5-4" stroke="#fff" fill="none"/></svg>info@corinnehalvers.com</li>
        <li><svg class="icon" viewBox="0 0 12 12"><circle cx="6" cy="6" r="5" fill="#1b5fb8"/><path d="M1 6h10M6 1c-2 2.5-2 7.5 0 10M6 1c2 2.5 2 7.5 0 10" stroke="#fff" stroke-width=".8" fill="none"/></svg>www.corinnehalvers.com</li>
      </ul>
    </div>

    <div class="recipient">
      <h2>Dear. Mrs Alma Reyes</h2>
      <p>Chief Director</p>
    </div>
    <div class="date">Date: 17-July-2025</div>

    <div class="letter-body">
      <p>Lorem ipsum dolor sit amet, consectetur adipiscing elit, sed do eiusmod tempor incididunt ut labore et dolore magna aliqua. Sollicitudin ac orci phasellus egestas tellus rutrum tellus. Euismod elementum nisi quis eleifend quam adipiscing vitae proin sagittis. Egestas sed tempus urna et pharetra pharetra. Quis blandit turpis cursus in hac habitasse. Sed velit dignissim sodales ut eu. Ac auctor augue mauris augue neque. In arcu cursus euismod quis viverra nibh cras pulvinar mattis. Libero justo laoreet sit amet. Felis eget nunc lobortis mattis aliquam faucibus purus in. Pulvinar etiam non quam lacus suspendisse faucibus. Odio tempor orci dapibus ultrices. Velit dignissim sodales ut eu sem integer vitae justo. Fermentum et sollicitudin ac orci phasellus egestas. Pharetra vel turpis nunc eget lorem dolor sed. Sed turpis tincidunt id aliquet risus feugiat in ante. Mus mauris vitae ultricies leo integer malesuada nunc vel. Rhoncus urna neque viverra justo nec ultrices dui. Ut placerat orci nulla pellentesque dignissim enim sit amet.</p>
      <p>Bibendum arcu vitae elementum curabitur vitae nunc. Nunc pulvinar sapien et ligula ullamcorper malesuada. At elementum eu facilisis sed. Erat pellentesque adipiscing commodo elit at imperdiet dui accumsan sit. Nunc scelerisque viverra mauris in aliquam sem fringilla. In vitae turpis massa sed. Volutpat ac tincidunt vitae semper quis lectus nulla at. Massa placerat duis ultricies lacus sed turpis. Dui vivamus arcu felis bibendum ut tristique et egestas. Blandit aliquam etiam erat velit scelerisque in dictum non consectetur. Id neque aliquam vestibulum morbi blandit cursus risus at. Sed egestas egestas fringilla phasellus faucibus scelerisque eleifend donec. Ornare quam viverra orci sagittis eu volutpat odio facilisis. Volutpat sed cras ornare arcu dui vivamus arcu. Interdum consectetur libero id faucibus nisl.</p>
      <p>Viverra mauris in aliquam sem. Mattis molestie a iaculis at erat pellentesque adipiscing commodo elit. Sit amet volutpat consequat mauris nunc. Aliquam nulla facilisi cras fermentum. Sed turpis tincidunt id aliquet risus feugiat. Augue neque gravida in fermentum et sollicitudin ac orci.</p>
    </div>

    <div class="signature" role="img" aria-label="Handwritten signature of Tobias Wren"></div>
    <div class="sign-off">
      <h3>Tobias Wren</h3>
      <p>Chief Director</p>
    </div>

    <div class="footer-band" role="img" aria-label="Decorative footer band in navy, blue and gold"></div>
  </section>

</main>
</body>
</html>
```